Website redesign www.tidecrestpc.com law firm site

Need to redesign the website that I currently have to look more modern and professional. Would also like to be able to make updates and post without having a huge hassle. See current www.tidecrestpc.com. I just think that it looks very immature and it's very templated there's no ability for me to make posts or Add links or anything like that

Target Market(s)

California people looking for a powerhouse attorney in

Industry/Entity Type

Legal

Number of Pages Required

3 page

Font styles to use
Serif
Sans Serif

Colors
ec1f27
000000
ffffff

Requirements
Must have
• Must be mobile friendly. Must look professional and have ability to post links to other websites. Must have ability to post blogs or articles. Would like to be able to read my TallyDock account and also have the ability to upload forms for people to download
Nice to have
• Simple design easy to use and not cluttered with too much text

```html
<!DOCTYPE html>
<html lang="en">
<head>
<meta charset="utf-8">
<title>Tidecrest Law, P.C. — Chico California Attorney</title>
<link rel="stylesheet" href="https://fonts.googleapis.com/css2?family=Noto+Serif:wght@400;700&family=Roboto:wght@300;400;500&display=swap">
<style>
:root{
  --red:#ec1f27;
  --red-dark:#b8161c;
  --ink:#1d1d1d;
  --text:#6a6a6a;
  --muted:#9a9a9a;
  --line:#e3e3e3;
  --paper:#ffffff;
  --mist:#f2f2f2;
  --nav:#3b3b3b;
  --navy:#1c2a44;
  --navy-deep:#142036;
  --serif:"Noto Serif", Georgia, serif;
  --sans:"Roboto", Arial, sans-serif;
}
*{box-sizing:border-box;margin:0;padding:0}
html,body{width:1200px;height:3396px;overflow:hidden}
body{font-family:var(--sans);color:var(--text);background:var(--paper);position:relative}
section,header,nav,footer{position:relative;width:1200px}
.ph{display:block}

/* top bar */
.topbar{height:95px;background:var(--paper)}
.topbar .contact{position:absolute;left:154px;top:26px;display:flex;gap:12px;align-items:flex-start}
.topbar .contact .num{font-size:17px;color:#444;line-height:20px}
.topbar .contact .mail{font-size:11px;color:#888}
.brand{position:absolute;left:0;right:0;top:30px;display:flex;justify-content:center;align-items:center;gap:10px}
.brand .mark{width:12px;height:12px;background:var(--red)}
.brand .name{font-family:var(--serif);font-weight:400;color:var(--red);font-size:28px;line-height:34px}
.btn-consult{position:absolute;right:154px;top:28px;border:1px solid #d6d6d6;border-radius:20px;padding:8px 18px;font-size:12px;color:#555;display:flex;gap:8px;align-items:center}

/* nav */
.mainnav{height:41px;background:var(--nav);border-bottom:3px solid #2a2a2a}
.mainnav ul{list-style:none;position:absolute;left:154px;width:892px;display:flex;justify-content:space-between;height:38px}
.mainnav li{font-family:var(--serif);color:#eee;font-size:14px;line-height:38px;padding:0 20px}
.mainnav li.active{background:var(--red)}

/* hero */
.hero{height:346px;background:linear-gradient(90deg,#f4f4f4 0%,#ececec 45%,#e4e4e4 70%,#f7f7f7 100%);overflow:hidden}
.hero .office{position:absolute;left:154px;top:20px;width:580px;height:310px;background:linear-gradient(180deg,rgba(200,200,200,.25),rgba(220,220,220,.1))}
.hero h1{position:absolute;left:166px;top:88px;width:560px;font-family:var(--serif);font-weight:400;color:var(--red);font-size:25px;line-height:33px}
.hero p{position:absolute;left:166px;top:166px;font-size:18px;color:#333}
.btn-outline{border:1px solid var(--red);border-radius:22px;color:#333;background:#fff;font-size:13px;padding:10px 20px;display:inline-block}
.hero .btn-outline{position:absolute;left:166px;top:212px}
.hero .portrait{position:absolute;left:754px;top:18px;width:236px;height:328px;border-radius:110px 110px 0 0;background:linear-gradient(180deg,#4a3a32 0%,#2d2d2d 45%,#222 100%)}
.arrow{position:absolute;width:34px;height:34px;border-radius:50%;border:1px solid #999;background:#fff;display:flex;align-items:center;justify-content:center}
.arrow.red{border-color:var(--red)}
.hero .prev{left:40px;top:154px}
.hero .next{left:1126px;top:154px}

/* about */
.about{height:424px;background:var(--mist)}
.about .frame{position:absolute;left:154px;top:57px;width:306px;height:306px;border-top:14px solid var(--red);border-left:14px solid var(--red)}
.about .photo{position:absolute;left:172px;top:75px;width:288px;height:288px;background:linear-gradient(160deg,#e9e4e0,#c9b7a6 60%,#b89a7e)}
.about .copy{position:absolute;left:536px;top:56px;width:510px}
.about .kicker{font-size:14px;color:#333}
.about h2{font-family:var(--serif);font-size:22px;color:var(--ink);margin:8px 0 18px;font-weight:700}
.about .copy p{font-size:12.5px;line-height:21px;color:#777;margin-bottom:14px}
.about .btn-grey{border:1px solid #aaa;border-radius:18px;font-size:12px;color:#555;padding:7px 18px;display:inline-block;margin-top:30px}

/* section headings */
.sec-head{position:absolute;left:0;right:0;text-align:center}
.sec-head h2{font-family:var(--serif);font-size:23px;color:var(--ink);font-weight:700;margin-top:10px}
.scale{display:block;margin:0 auto}

/* practice */
.practice{height:674px;background:var(--paper)}
.practice .sec-head{top:44px}
.grid{position:absolute;left:154px;top:131px;width:892px;display:grid;grid-template-columns:repeat(3,282px);column-gap:23px;row-gap:27px}
.card{height:204px;border:1px solid var(--line);text-align:center;padding-top:32px;background:#fff}
.card h3{font-family:var(--serif);font-weight:400;font-size:16px;color:#333;margin:10px 0 14px}
.card p{font-size:12px;line-height:17px;color:#888;padding:0 34px}
.card.featured{background:linear-gradient(180deg,#b8232b,#8f1419);border-color:var(--red-dark)}
.card.featured h3,.card.featured p{color:#fff}
.practice .btn-grey{position:absolute;left:530px;top:613px;width:140px;text-align:center;border:1px solid #aaa;border-radius:18px;font-size:12px;color:#555;padding:7px 0}

/* reviews */
.reviews{height:363px;background:var(--mist)}
.reviews .sec-head{top:50px}
.reviews .avatar{position:absolute;left:242px;top:147px;width:125px;height:125px;border-radius:50%;border:4px solid #fff;background:linear-gradient(160deg,#d7b48e,#8a5a3c)}
.reviews .quote{position:absolute;left:400px;top:143px}
.reviews .text{position:absolute;left:435px;top:157px;width:540px;font-size:12.5px;line-height:21px;color:#777}
.reviews .who{position:absolute;left:435px;top:276px}
.reviews .who b{display:block;font-weight:400;font-size:14px;color:#333;margin-bottom:6px}
.reviews .who b::before{content:"";display:inline-block;width:20px;height:1px;background:#555;vertical-align:middle;margin-right:10px}
.reviews .who span{font-size:11px;color:#888}
.reviews .prev{left:155px;top:191px}
.reviews .next{left:1010px;top:191px}

/* blog */
.blog{height:570px;background:#fff}
.blog .sec-head{top:54px}
.blog .feature{position:absolute;left:154px;top:158px;width:401px}
.blog .feature .img{height:204px;background:linear-gradient(160deg,#6d4a2a,#3a2716 55%,#1e140c)}
.date{position:absolute;width:42px;text-align:center;font-family:var(--serif);font-weight:700}
.date .d{background:var(--red);color:#fff;font-size:20px;line-height:32px}
.date .m{background:#ddd;color:#666;font-size:10px;line-height:14px;font-family:var(--sans);font-weight:400}
.blog .feature .date{left:0;top:0}
.blog .feature h3{font-family:var(--serif);font-weight:400;font-size:15px;color:#222;margin:20px 0 10px}
.meta{font-size:10px;color:#aaa;display:flex;gap:14px}
.blog .feature p{font-size:11.5px;line-height:16px;color:#888;margin-top:12px}
.more{font-size:11px;color:var(--red);margin-top:6px;display:block}
.blog .list{position:absolute;left:589px;top:158px;width:455px}
.post{position:relative;height:86px;background:#f2f2f2;margin-bottom:25px;padding:14px 16px 0 70px}
.post .date{left:0;top:22px}
.post h4{font-family:var(--serif);font-weight:400;font-size:13px;line-height:17px;color:#333;margin-bottom:6px}
.post.active h4{color:var(--red)}
.blog .list .more{color:#555;margin-top:0}

/* ratings */
.ratings{height:287px;background:var(--mist)}
.ratings .sec-head{top:52px}
.badges{position:absolute;left:196px;top:152px;width:810px;display:flex;justify-content:space-between;align-items:center}
.badge-seal{width:76px;height:76px;border-radius:50%;border:3px solid #777;background:#e6e6e6}
.badge-bar{width:210px;height:44px;background:#d7dce4}
.badge-bar.dark{background:#c9c9c9}
.badge-shield{width:86px;height:86px;border-radius:50%;border:4px solid #2b3d6e;background:#fff}
.badges .sep{width:1px;height:70px;background:#ccc}

/* footer */
.site-footer{height:510px;background:var(--navy)}
.info{position:absolute;top:56px;text-align:center;color:#fff;font-size:14px;line-height:20px}
.info .ico{width:40px;height:40px;border-radius:50%;background:#fff;margin:0 auto 16px;display:flex;align-items:center;justify-content:center}
.info.phone{left:234px;width:120px}
.info.addr{left:474px;width:220px}
.info.map{left:771px;width:160px}
.site-footer .rule{position:absolute;left:154px;width:914px;top:193px;height:1px;background:rgba(255,255,255,.18)}
.form-title{position:absolute;left:154px;top:243px;font-family:var(--serif);font-size:17px;color:#fff}
.field{position:absolute;left:154px;width:256px;height:32px;border:1px solid #8a93a6;border-radius:2px;font-size:11px;color:#e5e5e5;padding:9px 12px}
.field.area{left:428px;width:278px;height:126px}
.btn-send{position:absolute;left:154px;top:456px;background:#fff;color:#222;font-size:12px;border-radius:16px;padding:7px 14px;display:flex;gap:8px;align-items:center}
.sitelinks{position:absolute;left:840px;top:243px}
.sitelinks h4{font-family:var(--serif);font-weight:400;color:#fff;font-size:17px;margin-bottom:12px}
.sitelinks ul{list-style:none}
.sitelinks li{color:#fff;font-size:11px;line-height:24px}
.sitelinks li::before{content:"› ";}
.sitelinks li.current{color:var(--red)}
.social{display:flex;gap:9px;margin-top:20px}
.social span{width:24px;height:24px;border-radius:50%;border:1px solid #fff}
.bottombar{position:relative;width:1200px;height:86px;background:var(--navy-deep);border-top:1px solid rgba(255,255,255,.12)}
.bottombar .copy{position:absolute;left:154px;top:38px;font-size:11px;color:#ddd}
.bottombar .legal{position:absolute;right:160px;top:38px;font-size:11px;color:#ddd}
</style>
</head>
<body>

<header class="topbar">
  <div class="contact">
    <svg class="ph" width="24" height="24" viewBox="0 0 24 24"><circle cx="12" cy="12" r="11" fill="none" stroke="#ec1f27" stroke-width="2"/><path d="M8.5 7c.6-.5 1.3-.4 1.6.2l.9 1.7c.2.5.1 1-.3 1.3l-.6.5c.6 1.3 1.5 2.2 2.8 2.8l.5-.6c.3-.4.8-.5 1.3-.3l1.7.9c.6.3.7 1 .2 1.6-1 1.1-2.4 1.3-4 .4-2-1.1-3.5-2.6-4.6-4.6-.8-1.6-.6-3 .5-3.9z" fill="#ec1f27"/></svg>
    <div><div class="num">(530) 555-0142</div><div class="mail">info@tidecrestlaw.com</div></div>
  </div>
  <div class="brand"><span class="mark"></span><span class="name">Tidecrest Law, P.C.</span></div>
  <div class="btn-consult">
    <svg width="14" height="12" viewBox="0 0 14 12"><path d="M1 1h9v6H5l-3 3V7H1z" fill="#ec1f27"/><path d="M11 4h2v5h-1v2l-2-2H6V8h5z" fill="#ec1f27"/></svg>
    Free Consultations
  </div>
</header>

<nav class="mainnav">
  <ul>
    <li class="active">Home</li>
    <li>Attorney Profile</li>
    <li>Practice Areas ▾</li>
    <li>Client Reviews</li>
    <li>Links&amp;Forms</li>
    <li>Contact Us</li>
  </ul>
</nav>

<section class="hero">
  <div class="office" role="img" aria-label="Faded photo of a meeting in a law office"></div>
  <h1>Practical Law saves us time, thereby increasing our ability to service clients.</h1>
  <p>Lorem ipsum dolor sit amet, consectetur adipiscing elit</p>
  <span class="btn-outline">Contact Us</span>
  <div class="portrait" role="img" aria-label="Photo of the attorney in a dark suit, arms crossed"></div>
  <span class="arrow prev"><svg width="10" height="12" viewBox="0 0 10 12"><path d="M7 1L2 6l5 5" fill="none" stroke="#555" stroke-width="1.6"/></svg></span>
  <span class="arrow next red"><svg width="10" height="12" viewBox="0 0 10 12"><path d="M3 1l5 5-5 5" fill="none" stroke="#ec1f27" stroke-width="1.6"/></svg></span>
</section>

<section class="about">
  <div class="frame"></div>
  <div class="photo" role="img" aria-label="Portrait photo of attorney Dana R. Whitlow"></div>
  <div class="copy">
    <div class="kicker">Tidecrest Law, P.C.</div>
    <h2>Chico California Attorney</h2>
    <p>Find the big firm style legal counsel you can work with in your hometown region at Tidecrest Law P.C., in Chico, CA. Attorney Dana R. Whitlow, Esq., offers a boutique law firm opportunity for clients who want to enjoy all the advantages of her broad legal experience and education. She works closely with clients, and has the knowledge of many areas of law to apply to your situation.</p>
    <p>This is very helpful when it is necessary to incorporate those different areas of law practice into creating a winning argument for your unique case.</p>
    <span class="btn-grey">Discover About Us</span>
  </div>
</section>

<section class="practice">
  <div class="sec-head">
    <svg class="scale" width="30" height="22" viewBox="0 0 30 22"><path d="M15 2v16M6 5h18M6 5l-4 8h8zM24 5l-4 8h8zM9 19h12" fill="none" stroke="#ec1f27" stroke-width="1.6"/><path d="M2 13a4 2 0 0 0 8 0zM20 13a4 2 0 0 0 8 0z" fill="#ec1f27"/></svg>
    <h2>Practice areas</h2>
  </div>
  <div class="grid">
    <div class="card">
      <svg width="40" height="34" viewBox="0 0 40 34"><rect x="3" y="9" width="34" height="23" rx="3" fill="#8a8a8a"/><rect x="14" y="3" width="12" height="7" rx="2" fill="none" stroke="#8a8a8a" stroke-width="3"/></svg>
      <h3>Business Law</h3>
      <p>Small and medium sized businesses have many of the same legal issues that affect large businesse.</p>
    </div>
    <div class="card featured" role="group" aria-label="Real Estate Law, shown over a photo of a house">
      <svg width="40" height="36" viewBox="0 0 40 36"><path d="M4 18L20 4l16 14" fill="none" stroke="#fff" stroke-width="3"/><path d="M9 16v17h22V16" fill="none" stroke="#fff" stroke-width="3"/><circle cx="20" cy="22" r="6" fill="none" stroke="#fff" stroke-width="2"/></svg>
      <h3>Real Estate Law</h3>
      <p>At Tidecrest Law P.C., we help Californians who need legal advice and representation for Real Estate...</p>
    </div>
    <div class="card">
      <svg width="40" height="36" viewBox="0 0 40 36"><rect x="8" y="6" width="16" height="9" transform="rotate(-40 16 10)" fill="#8a8a8a"/><path d="M18 16l14 16" stroke="#8a8a8a" stroke-width="4"/></svg>
      <h3>Bankruptcy</h3>
      <p>If your finances are dwindling to the point where you can no longer pay your bills, and you are getting...</p>
    </div>
    <div class="card">
      <svg width="44" height="34" viewBox="0 0 44 34"><circle cx="22" cy="9" r="6" fill="#8a8a8a"/><circle cx="9" cy="13" r="5" fill="#8a8a8a"/><circle cx="35" cy="13" r="5" fill="#8a8a8a"/><path d="M12 32c0-9 20-9 20 0zM1 32c0-7 14-7 14-2v2zM29 32v-2c0-5 14-5 14 2z" fill="#8a8a8a"/></svg>
      <h3>Family Law</h3>
      <p>Family Law is one area of legal concern that brings many people in to see our experienced...</p>
    </div>
    <div class="card">
      <svg width="48" height="34" viewBox="0 0 48 34"><circle cx="13" cy="20" r="10" fill="none" stroke="#8a8a8a" stroke-width="3"/><circle cx="35" cy="20" r="10" fill="none" stroke="#8a8a8a" stroke-width="3"/><path d="M20 12q4-8 8 0" fill="none" stroke="#8a8a8a" stroke-width="3"/></svg>
      <h3>Criminal Law</h3>
      <p>Chico Criminal Law Attorney If you were charged with a criminal offense, or if you are under...</p>
    </div>
    <div class="card">
      <svg width="40" height="36" viewBox="0 0 40 36"><rect x="10" y="4" width="18" height="9" transform="rotate(35 19 8)" fill="#8a8a8a"/><path d="M20 14l-10 12" stroke="#8a8a8a" stroke-width="4"/><rect x="6" y="29" width="28" height="5" fill="#8a8a8a"/></svg>
      <h3>Civil Litigation</h3>
      <p>Civil Litigation is a vast legal category than can include everything from personal injury cases...</p>
    </div>
  </div>
  <span class="btn-grey">View All Practices</span>
</section>

<section class="reviews">
  <div class="sec-head">
    <svg class="scale" width="30" height="22" viewBox="0 0 30 22"><path d="M15 2v16M6 5h18M6 5l-4 8h8zM24 5l-4 8h8zM9 19h12" fill="none" stroke="#ec1f27" stroke-width="1.6"/><path d="M2 13a4 2 0 0 0 8 0zM20 13a4 2 0 0 0 8 0z" fill="#ec1f27"/></svg>
    <h2>Client Reviews</h2>
  </div>
  <span class="arrow prev"><svg width="10" height="12" viewBox="0 0 10 12"><path d="M7 1L2 6l5 5" fill="none" stroke="#555" stroke-width="1.6"/></svg></span>
  <div class="avatar" role="img" aria-label="Round portrait photo of the reviewer"></div>
  <svg class="quote" width="24" height="18" viewBox="0 0 24 18"><path d="M2 18V10Q2 2 9 1v3Q6 5 6 9h4v9zM14 18V10q0-8 7-9v3q-3 1-3 5h4v9z" fill="#555"/></svg>
  <p class="text">Tidecrest Law is our go to source for professional and sound legal advice. Tidecrest Law has become a vital component to the success of our business as well as the businesses of the clients we have referred to Tidecrest Law professional and sound legal advice. Tidecrest Law has become a vital.</p>
  <div class="who"><b>A Vital Component</b><span>Orchard Lane Accounting Group</span></div>
  <span class="arrow next red"><svg width="10" height="12" viewBox="0 0 10 12"><path d="M3 1l5 5-5 5" fill="none" stroke="#ec1f27" stroke-width="1.6"/></svg></span>
</section>

<section class="blog">
  <div class="sec-head">
    <svg class="scale" width="30" height="22" viewBox="0 0 30 22"><path d="M15 2v16M6 5h18M6 5l-4 8h8zM24 5l-4 8h8zM9 19h12" fill="none" stroke="#ec1f27" stroke-width="1.6"/><path d="M2 13a4 2 0 0 0 8 0zM20 13a4 2 0 0 0 8 0z" fill="#ec1f27"/></svg>
    <h2>Our Latest Blog</h2>
  </div>
  <article class="feature">
    <div class="img" role="img" aria-label="Photo of a gavel and brass scales on law books"></div>
    <div class="date"><div class="d">25</div><div class="m">Jun</div></div>
    <h3>Criminal liability of an enterprise</h3>
    <div class="meta"><span>Posted By: John Smith</span><span>View:65</span><span>Comment:174</span></div>
    <p>Lorem Ipsum is simply dummy text of the printing and typesetting industry. Lorem Ipsum has been the industry's standard dummy text ever since Lorem Ipsum is simply dummy.</p>
    <span class="more">» Read More</span>
  </article>
  <div class="list">
    <article class="post"><div class="date"><div class="d">26</div><div class="m">Aug</div></div><h4>Useless laws weaken the necessary laws. reach if you just keep climbing</h4><div class="meta"><span>Posted By: John Smith</span><span>View:65</span><span>Comment:174</span></div></article>
    <article class="post active"><div class="date"><div class="d">27</div><div class="m">Aug</div></div><h4>Every mountain top is within reach if you just keep climbing</h4><div class="meta"><span>Posted By: John Smith</span><span>View:65</span><span>Comment:174</span></div></article>
    <article class="post"><div class="date"><div class="d">28</div><div class="m">Aug</div></div><h4>Useless laws weaken the necessary laws. reach if you just keep climbing</h4><div class="meta"><span>Posted By: John Smith</span><span>View:65</span><span>Comment:174</span></div></article>
    <span class="more">» More Blog</span>
  </div>
</section>

<section class="ratings">
  <div class="sec-head">
    <svg class="scale" width="30" height="22" viewBox="0 0 30 22"><path d="M15 2v16M6 5h18M6 5l-4 8h8zM24 5l-4 8h8zM9 19h12" fill="none" stroke="#ec1f27" stroke-width="1.6"/><path d="M2 13a4 2 0 0 0 8 0zM20 13a4 2 0 0 0 8 0z" fill="#ec1f27"/></svg>
    <h2>Ratings and Reviews</h2>
  </div>
  <div class="badges">
    <div class="badge-seal" role="img" aria-label="Bar association seal"></div>
    <span class="sep"></span>
    <div class="badge-bar" role="img" aria-label="Lawyer directory listing badge"></div>
    <span class="sep"></span>
    <div class="badge-bar dark" role="img" aria-label="Partner company badge"></div>
    <span class="sep"></span>
    <div class="badge-shield" role="img" aria-label="Attorney rating badge"></div>
  </div>
</section>

<footer class="site-footer">
  <div class="info phone"><div class="ico"><svg width="16" height="16" viewBox="0 0 24 24"><path d="M6 3c1-1 2-.8 2.6.3l1.5 2.8c.4.8.2 1.6-.5 2.1l-1 .8c1 2.2 2.6 3.8 4.7 4.7l.8-1c.5-.7 1.3-.9 2.1-.5l2.8 1.5c1 .6 1.2 1.7.3 2.6-1.7 1.8-4 2.1-6.6.7-3.3-1.8-5.800-4.3-7.6-7.6C3.8 7 4.200 4.7 6 3z" fill="#ec1f27"/></svg></div>(530) 555-0142</div>
  <div class="info addr"><div class="ico"><svg width="16" height="16" viewBox="0 0 16 16"><path d="M14 2L2 7l5 2 2 5z" fill="#ec1f27"/></svg></div>218 Cedar Avenue<br>Suite 410, Chico, CA 95900</div>
  <div class="info map"><div class="ico"><svg width="14" height="18" viewBox="0 0 14 18"><path d="M7 1a6 6 0 0 1 6 6c0 4-6 10-6 10S1 11 1 7a6 6 0 0 1 6-6z" fill="#ec1f27"/><circle cx="7" cy="7" r="2.2" fill="#fff"/></svg></div>Map and Directions</div>
  <div class="rule"></div>
  <div class="form-title">Request Your Free Consulation</div>
  <div class="field" style="top:290px">Name</div>
  <div class="field" style="top:338px">Email</div>
  <div class="field" style="top:385px">Phone Number</div>
  <div class="field area" style="top:290px">Describe your case</div>
  <div class="btn-send">Send <svg width="14" height="12" viewBox="0 0 14 12"><path d="M13 1L1 5l4 2 1 4z" fill="#1c2a44"/></svg></div>
  <div class="sitelinks">
    <h4>Site Links</h4>
    <ul>
      <li>Home</li>
      <li class="current">Attorney Profile</li>
      <li>Practice Areas</li>
      <li>Client Reviews</li>
      <li>Contact Us</li>
    </ul>
    <div class="social"><span></span><span></span><span></span></div>
  </div>
</footer>

<div class="bottombar">
  <div class="copy">© 2016 Tidecrest Law, P.C. All Rights Reserved</div>
  <div class="legal">Disclaimer &nbsp;/&nbsp; Site Map &nbsp;/&nbsp; Sign In</div>
</div>

</body>
</html>
```